Children's writer business card design

I write children's mystery and adventure books for 9-12 year olds. My logo is a small robin redbreast bird which I will appear on all my commercial stationery and websites. I have a 'silhouette' of a bird on the mock up on your site and I like this, although your designers might make it look even better. The bird is non-negotiable!

When I tried to do the back of the card I got a hallmark. I don't like this.

I would like the card to be modern, 'clean' and striking. Not too much colour. Definitely the red for the bird so it really stands out.

Target Market(s)

parents and grandparents of children 9-12 years old, booksellers, teachers

Industry/Entity Type

Business

Contact Information for Business Card

I have created a rough design using Cardlyne which I hope you can access as this contains all of the information I want on my card.
The front has the following:
Maren Talbot
Writer & Education Consultant
www.marentalbotwriter.example

04915360284
mtalwex@quillmail.example

The back has:
Books
The Garnet Locket Puzzles (In bold)
The Riddle of the Garnet Locket (in italics)
The Whisper of the Garnet (italics)
The Pomfrey Project (in bold)
Book 1: Stuck (italics)
Book 2: Unstuck (italics)

I'm happy for you to change the design provided the 'robin' stays.
Thank you.

Colors
ec2027

Requirements
Must have
• the robin redbreast bird logo - although it is fine to change how the bird looks.
Should not have
• no watermark

```html
<!DOCTYPE html>
<html lang="en">
<head>
<meta charset="utf-8">
<title>Maren Talbot – Business Card</title>
<link rel="stylesheet" href="https://fonts.googleapis.com/css2?family=Arimo:wght@700&family=Gochi+Hand&family=Carlito&family=Open+Sans:ital,wght@0,400;0,700;1,400&display=swap">
<style>
  :root {
    --backdrop: #2b2b2b;
    --card-black: #050505;
    --card-white: #ffffff;
    --ink-white: #ffffff;
    --ink-dark: #111111;
    --robin-red: #ec2027;
  }
  * { box-sizing: border-box; margin: 0; padding: 0; }
  html, body {
    width: 1200px;
    height: 930px;
    overflow: hidden;
    background: var(--backdrop);
  }
  .canvas {
    width: 1200px;
    height: 930px;
    display: flex;
    align-items: center;
    justify-content: center;
    gap: 50px;
  }
  .card {
    width: 525px;
    height: 300px;
    position: relative;
    flex: none;
  }

  /* Front */
  .card-front {
    background: var(--card-black);
    color: var(--ink-white);
    text-align: center;
  }
  .brand {
    position: absolute;
    top: 52px;
    left: 0;
    right: 0;
    display: flex;
    justify-content: center;
    align-items: center;
    gap: 10px;
  }
  .brand-name {
    font-family: "Arimo", Arial, sans-serif;
    font-weight: 700;
    font-size: 54px;
    letter-spacing: -1px;
    line-height: 1;
    color: var(--ink-white);
  }
  .brand-dot { width: 14px; height: 14px; flex: none; }
  .tagline {
    position: absolute;
    top: 124px;
    left: 0;
    right: 0;
    font-family: "Gochi Hand", cursive;
    font-size: 24px;
    letter-spacing: 0.5px;
  }
  .contact {
    position: absolute;
    top: 198px;
    left: 0;
    right: 0;
    list-style: none;
    font-family: "Carlito", Calibri, sans-serif;
    font-size: 17px;
    line-height: 25px;
  }

  /* Back */
  .card-back {
    background: var(--card-white);
    color: var(--ink-dark);
    font-family: "Open Sans", Verdana, sans-serif;
    display: flex;
    align-items: flex-start;
    padding: 44px 28px 0 24px;
  }
  .series {
    width: 290px;
    text-align: center;
    font-size: 13px;
    line-height: 1.4;
    padding-top: 50px;
  }
  .series-title { font-weight: 700; }
  .series-book { font-style: italic; }
  .series-title + .series-book { margin-top: 10px; }
  .series-book + .series-title { margin-top: 22px; }
  .divider {
    width: 3px;
    height: 150px;
    background: var(--robin-red);
    margin: 0 18px 0 14px;
    flex: none;
  }
  .standalone {
    list-style: none;
    font-size: 14px;
    font-style: italic;
    line-height: 1;
  }
  .standalone li + li { margin-top: 20px; }
</style>
</head>
<body>
<main class="canvas">
  <section class="card card-front" aria-label="Business card front">
    <div class="brand">
      <span class="brand-name">Maren Talbot</span>
      <svg class="brand-dot" viewBox="0 0 14 14" aria-hidden="true"><circle cx="7" cy="7" r="7" fill="var(--robin-red)"/></svg>
    </div>
    <p class="tagline">Maren Talbot Writer &amp; Education Consultant</p>
    <ul class="contact">
      <li>04915360284</li>
      <li>mtalwex@quillmail.example</li>
      <li>www.marentalbotwriter.example</li>
    </ul>
  </section>

  <section class="card card-back" aria-label="Business card back">
    <div class="series">
      <p class="series-title">Books The Garnet Locket Puzzles</p>
      <p class="series-book">The Riddle of the Garnet Locket</p>
      <p class="series-book">The Whisper of the Garnet</p>
      <p class="series-title">The Pomfrey Project</p>
    </div>
    <div class="divider"></div>
    <ul class="standalone">
      <li>Book 1: Stuck</li>
      <li>Book 2: Unstuck</li>
    </ul>
  </section>
</main>
</body>
</html>
```